K.Wren Customer Retention Business Infographic

I am looking to create an infographic by transforming the following data to be used on my website and proposals. I have specific colors that I would like to blend with and a concept of what it could look like, but open. I want to be able to show the comparison...of the two data points side by side.

Target Market(s)

Passionate Business owners

Industry/Entity Type

Business consulting

Font styles to use
Sans Serif

Requirements
Must have
• Concise infographic side by side comparision to use on website and proposals

```html
<!DOCTYPE html>
<html lang="en">
<head>
<meta charset="utf-8">
<title>K.Wren Customer Retention Infographic</title>
<link rel="stylesheet" href="https://fonts.googleapis.com/css2?family=Bebas+Neue&family=Source+Sans+3:ital,wght@0,400;0,600;0,700;1,400&display=swap">
<style>
  :root {
    --backdrop: #000000;
    --navy: #13295b;
    --navy-deep: #0b1d44;
    --slate: #5f77a3;
    --slate-deep: #3f5783;
    --mist: #b3bdd3;
    --mist-deep: #8e9bb8;
    --panel-cool: #eff2f7;
    --panel-warm: #ffffff;
    --lead-cool: #6b82a8;
    --orange: #f7941d;
    --step-1: #fcd660;
    --step-2: #fbc35f;
    --step-3: #f9a847;
    --step-4: #f7902a;
    --fold: #d9801a;
    --fold-deep: #b86410;
    --icon-warm: #f9b233;
    --band: #f8c944;
    --ink: #13295b;
    --credit: #3b4a66;
  }
  html, body {
    margin: 0;
    padding: 0;
    width: 1200px;
    height: 1200px;
    overflow: hidden;
    background: var(--backdrop);
  }
  .infographic {
    position: absolute;
    left: 71px;
    top: 186px;
    width: 1070px;
    height: 828px;
    display: block;
  }
  .title { font-family: "Bebas Neue", "Oswald", sans-serif; font-size: 57px; }
  .title-light { fill: #ffffff; }
  .title-accent { fill: var(--orange); }
  .lead { font-family: "Source Sans 3", "Helvetica Neue", sans-serif; font-size: 16.5px; font-weight: 700; fill: var(--ink); }
  .lead-cool { fill: var(--lead-cool); }
  .lead-warm { fill: var(--orange); }
  .step-text { font-family: "Source Sans 3", "Helvetica Neue", sans-serif; font-size: 11px; font-weight: 700; text-anchor: middle; }
  .on-dark { fill: #ffffff; }
  .on-light { fill: var(--ink); }
  .credit { font-family: "Source Sans 3", "Helvetica Neue", sans-serif; font-size: 10px; font-style: italic; fill: var(--credit); text-anchor: end; }
  .icon-cool { fill: none; stroke-width: 2; stroke-linecap: round; stroke-linejoin: round; }
  .icon-warm { fill: none; stroke: var(--icon-warm); stroke-width: 2; stroke-linecap: round; stroke-linejoin: round; }
</style>
</head>
<body>
<svg class="infographic" viewBox="0 0 892 690" xmlns="http://www.w3.org/2000/svg">
  <!-- header -->
  <rect class="header-band" x="0" y="0" width="892" height="110" fill="var(--navy)"/>
  <text class="title" x="446" y="76" text-anchor="middle"><tspan class="title-light">WHEN CUSTOMERS ENGAGE </tspan><tspan class="title-accent">BUSINESSES FLOURISH</tspan></text>

  <!-- panels -->
  <rect class="panel-cost" x="0" y="110" width="416" height="568" fill="var(--panel-cool)"/>
  <rect class="panel-gain" x="416" y="110" width="476" height="568" fill="var(--panel-warm)"/>
  <rect class="footer-band" x="0" y="678" width="892" height="12" fill="var(--band)"/>

  <!-- cost side heading -->
  <g class="lead" text-anchor="end">
    <text x="389" y="152" class="lead lead-cool">When your customers are not ecstatic,</text>
    <text x="389" y="177" class="lead">you are stuck with stagnant growth</text>
    <text x="389" y="202" class="lead">and dropping retention rate…</text>
    <text x="389" y="227" class="lead">it costs you</text>
  </g>

  <!-- cost side steps -->
  <g class="cost-steps">
    <rect x="130" y="398" width="60" height="99" fill="var(--navy-deep)"/>
    <rect x="230" y="460" width="55" height="100" fill="var(--slate-deep)"/>
    <path d="M71 380 a45 45 0 0 1 90 0 V497 H71 Z" fill="var(--navy)"/>
    <path d="M169 443 a45 45 0 0 1 90 0 V560 H169 Z" fill="var(--slate)"/>
    <path d="M261 505 a46 46 0 0 1 92 0 V615 H373 L307 657 L246 615 H261 Z" fill="var(--mist)"/>
  </g>
  <text class="step-text on-dark" x="116" y="375">5% to 20%</text>
  <text class="step-text on-dark" x="116" y="390">probability</text>
  <text class="step-text on-dark" x="116" y="405">of selling to</text>
  <text class="step-text on-dark" x="116" y="420">a new</text>
  <text class="step-text on-dark" x="116" y="435">prospect</text>

  <text class="step-text on-dark" x="213" y="442">Costs</text>
  <text class="step-text on-dark" x="213" y="457">16 times more</text>
  <text class="step-text on-dark" x="213" y="472">to build</text>
  <text class="step-text on-dark" x="213" y="487">a long-term</text>
  <text class="step-text on-dark" x="213" y="502">relationship</text>
  <text class="step-text on-dark" x="213" y="517">with a new</text>
  <text class="step-text on-dark" x="213" y="532">customer.</text>

  <text class="step-text on-dark" x="309" y="485">5x higher cost</text>
  <text class="step-text on-dark" x="309" y="501">to acquire</text>
  <text class="step-text on-dark" x="309" y="517">new customers</text>
  <text class="step-text on-dark" x="309" y="533">than retain</text>
  <text class="step-text on-dark" x="309" y="549">existing ones</text>

  <!-- cost side icons -->
  <g class="icon-cool" stroke="var(--navy)">
    <rect x="106" y="272" width="20" height="20" rx="2"/>
    <path d="M111 276 a5 5 0 0 0 10 0"/>
    <path d="M90 310 h12 l12 8 h18 l14 -12 M102 310 v12 h10 l14 6 h6"/>
  </g>
  <g class="icon-cool" stroke="var(--slate)">
    <path d="M196 340 h20 l6 8 v28 h-26 Z"/>
    <path d="M212 352 h20 l6 8 v24 h-26 Z"/>
    <text x="206" y="366" font-family="Source Sans 3, sans-serif" font-size="14" font-weight="700" fill="var(--slate)" stroke="none" text-anchor="middle">$</text>
  </g>
  <g class="icon-cool" stroke="var(--mist-deep)">
    <path d="M286 410 v-8 h8 M328 402 h8 v8 M336 436 v8 h-8 M294 444 h-8 v-8"/>
    <circle cx="301" cy="418" r="4"/><circle cx="311" cy="414" r="4"/><circle cx="321" cy="418" r="4"/>
    <path d="M294 436 a7 7 0 0 1 14 0 M304 432 a7 7 0 0 1 14 0 M314 436 a7 7 0 0 1 14 0"/>
  </g>

  <!-- gain side heading -->
  <text x="446" y="152" class="lead lead-warm">When your customers are happy</text>
  <text x="446" y="177" class="lead">and your business becomes</text>
  <text x="446" y="202" class="lead">an essential part of their lives…</text>
  <text x="446" y="227" class="lead">you experience</text>

  <!-- gain side steps -->
  <g class="gain-steps">
    <rect x="530" y="465" width="60" height="92" fill="var(--fold)"/>
    <rect x="630" y="403" width="60" height="92" fill="var(--fold)"/>
    <rect x="725" y="340" width="60" height="92" fill="var(--fold-deep)"/>
    <path d="M466 510 a45 45 0 0 1 90 0 V627 H466 Z" fill="var(--step-1)"/>
    <path d="M566 448 a44 44 0 0 1 88 0 V555 H566 Z" fill="var(--step-2)"/>
    <path d="M663 385 a45 45 0 0 1 90 0 V497 H663 Z" fill="var(--step-3)"/>
    <path d="M756 285 H744 L806 230 L869 285 H846 V395 a45 45 0 0 1 -90 0 Z" fill="var(--step-4)"/>
  </g>
  <text class="step-text on-light" x="511" y="505">65% of</text>
  <text class="step-text on-light" x="511" y="520">your business</text>
  <text class="step-text on-light" x="511" y="535">comes from</text>
  <text class="step-text on-light" x="511" y="550">repeat</text>
  <text class="step-text on-light" x="511" y="565">customers.</text>

  <text class="step-text on-light" x="610" y="427">60% of</text>
  <text class="step-text on-light" x="610" y="442">loyal</text>
  <text class="step-text on-light" x="610" y="457">customers</text>
  <text class="step-text on-light" x="610" y="472">will talk</text>
  <text class="step-text on-light" x="610" y="487">about YOU</text>
  <text class="step-text on-light" x="610" y="502">with their</text>
  <text class="step-text on-light" x="610" y="517">friends</text>
  <text class="step-text on-light" x="610" y="532">and family.</text>

  <text class="step-text on-light" x="709" y="377">60-70%</text>
  <text class="step-text on-light" x="709" y="392">probability</text>
  <text class="step-text on-light" x="709" y="407">of selling to</text>
  <text class="step-text on-light" x="709" y="422">an existing</text>
  <text class="step-text on-light" x="709" y="437">customer</text>

  <text class="step-text on-dark" x="801" y="330">Boost profits</text>
  <text class="step-text on-dark" x="801" y="345">by 25% to 95%</text>
  <text class="step-text on-dark" x="801" y="360">with</text>
  <text class="step-text on-dark" x="801" y="375">5% increase</text>
  <text class="step-text on-dark" x="801" y="390">in customer</text>
  <text class="step-text on-dark" x="801" y="405">retention.</text>

  <!-- gain side icons -->
  <g class="icon-warm">
    <circle cx="502" cy="400" r="4"/><circle cx="514" cy="396" r="4"/><circle cx="526" cy="400" r="4"/>
    <path d="M495 418 a7 7 0 0 1 14 0 M507 414 a7 7 0 0 1 14 0 M519 418 a7 7 0 0 1 14 0"/>
    <path d="M486 396 v18 l14 22 v8 M542 396 v18 l-14 22 v8"/>
  </g>
  <g class="icon-warm">
    <circle cx="611" cy="340" r="10"/><circle cx="593" cy="375" r="10"/><circle cx="629" cy="375" r="10"/>
    <path d="M611 350 v10 l-10 6 M611 360 l10 6"/>
  </g>
  <g class="icon-warm">
    <path d="M684 290 h14 l12 -8 h10 l14 10 M684 300 h10 l14 10 h12 l14 -10"/>
    <path d="M690 318 h16 l14 6 h14"/>
  </g>
  <g class="icon-warm">
    <path d="M792 210 v-20 m-6 6 l6 -8 l6 8 M807 205 v-20 m-6 6 l6 -8 l6 8 M822 210 v-20 m-6 6 l6 -8 l6 8"/>
    <circle cx="807" cy="225" r="11"/>
    <text x="807" y="230" font-family="Source Sans 3, sans-serif" font-size="13" font-weight="700" fill="var(--icon-warm)" stroke="none" text-anchor="middle">$</text>
  </g>

  <text class="credit" x="853" y="664">Icons by Iconhaus from Glyphbank.com</text>
</svg>
</body>
</html>
```